Full Page Appliance Ad

Create a full page ad (7.5" W x 10" H) representing that we are a full service appliance company, where we have a showroom located at 14 N. Larkmoor Avenue Fernwick, PA 18977. Our website is www.qbtrevolt.com , and our phone number is 215-846-3190. We don't only sell appliances, we deliver, install, and service. We also offer an additional year warranty* (see store for details). In addition to appliances, we also have an Electrical Department that specializes in residential applications.
May be best if split the full page ad into two spots. One spot to reference appliances, and the other to represent electrical.
I want it to look clean, and not too busy
30-70 years old

```html
<!DOCTYPE html>
<html lang="en">
<head>
<meta charset="UTF-8">
<title>Qbtrevolt – Full Service Appliance Company</title>
<link href="https://fonts.googleapis.com/css2?family=Poppins:wght@400;500;600;700;800&display=swap" rel="stylesheet">
<style>
  :root {
    --navy: #11122e;
    --sky: #b3cdea;
    --sky-light: #dce8f7;
    --charcoal: #333333;
    --body-grey: #595d63;
    --white: #ffffff;
    --rule: #2a2a3a;
  }
  * { margin: 0; padding: 0; box-sizing: border-box; }
  html, body { width: 900px; height: 1200px; overflow: hidden; background: var(--white); }
  body { font-family: "Poppins", sans-serif; color: var(--navy); }
  .ad { position: relative; width: 900px; height: 1200px; overflow: hidden; background: var(--white); }

  .hero-bg { position: absolute; inset: 0 0 auto 0; height: 600px;
    background: linear-gradient(180deg, var(--sky) 0%, var(--sky-light) 100%); }
  .hero-photo { position: absolute; left: 382px; top: 95px; width: 518px; height: 420px;
    background: linear-gradient(135deg, #c9d5e4 0%, #9fb2ca 55%, #7f93ad 100%); }
  .hero-shape { position: absolute; left: 0; top: 0; }

  .brand { position: absolute; left: 60px; top: 46px; display: flex; align-items: center; gap: 16px; }
  .brand-dot { width: 86px; height: 86px; border-radius: 50%; border: 5px solid var(--navy); }
  .brand-name { font-weight: 700; font-size: 38px; line-height: 1; color: var(--navy); letter-spacing: 0.5px; }

  .headline { position: absolute; left: 60px; top: 168px; font-weight: 800; color: var(--navy); }
  .headline .line-1 { display: block; font-size: 62px; line-height: 72px; letter-spacing: -0.5px; }
  .headline .line-2 { display: block; font-size: 38px; line-height: 56px; letter-spacing: -0.3px; }
  .showroom { position: absolute; left: 60px; top: 296px; font-size: 15.5px; font-weight: 500; line-height: 30px; color: var(--navy); }

  .web-pill { position: absolute; left: 60px; top: 372px; width: 246px; height: 48px; border-radius: 24px;
    background: var(--charcoal); display: flex; align-items: center; }
  .web-pill .globe { width: 44px; height: 44px; margin-left: 2px; border-radius: 50%; background: var(--navy);
    display: flex; align-items: center; justify-content: center; }
  .web-pill span { color: var(--white); font-weight: 600; font-size: 15px; margin-left: 20px; }

  .center-badge { position: absolute; left: 547px; top: 519px; width: 94px; height: 94px; border-radius: 50%;
    background: var(--white); box-shadow: 0 0 0 14px rgba(245,245,248,0.75); }

  .section-title { position: absolute; left: 60px; font-weight: 800; font-size: 25px; line-height: 30px; color: var(--navy); letter-spacing: -0.2px; }
  .copy { position: absolute; font-size: 12px; line-height: 25px; color: var(--body-grey); text-align: justify; }

  .fridge-photo { position: absolute; left: 302px; top: 978px; width: 155px; height: 212px;
    background: linear-gradient(90deg, #c8c8c8 0%, #9a9a9a 45%, #1c1c1c 48%, #0c0c0c 100%); }

  .footer-band { position: absolute; left: 0; top: 1077px; width: 302px; height: 123px; background: var(--navy); }
  .footer-band .pin { position: absolute; left: 60px; top: 35px; }
  .footer-band address { position: absolute; left: 105px; top: 34px; font-style: normal; color: var(--white);
    font-size: 13.5px; line-height: 25px; }

  .provide-pill { position: absolute; left: 484px; top: 658px; width: 416px; height: 53px; background: var(--navy);
    border-radius: 27px 0 0 27px; color: var(--white); font-weight: 800; font-size: 25px; line-height: 53px; padding-left: 39px; }

  .services { position: absolute; left: 484px; top: 939px; display: flex; gap: 25px; }
  .service { width: 70px; text-align: center; }
  .service-icon { width: 70px; height: 70px; border-radius: 50%; background: var(--navy); border: 5px solid var(--charcoal);
    box-shadow: inset 0 0 0 3px var(--white); display: flex; align-items: center; justify-content: center; }
  .service-label { margin-top: 13px; font-size: 11.5px; font-weight: 600; color: var(--navy); white-space: nowrap; margin-left: -15px; margin-right: -15px; }

  .divider { position: absolute; left: 490px; top: 1074px; width: 348px; height: 1px; background: var(--rule); }

  .call { position: absolute; left: 578px; top: 1110px; display: flex; align-items: center; gap: 26px; }
  .call-label { font-size: 11.5px; font-weight: 600; color: var(--navy); }
  .call-number { font-size: 29px; font-weight: 800; color: var(--navy); line-height: 38px; letter-spacing: -0.3px; }

  .bottom-strip { position: absolute; left: 405px; top: 1193px; width: 495px; height: 7px; background: var(--navy); }
</style>
</head>
<body>
<main class="ad">
  <div class="hero-bg"></div>
  <div class="hero-photo" role="img" aria-label="Photo of stainless steel appliances: washer, refrigerator, microwave with blender, dishwasher and oven"></div>

  <svg class="hero-shape" width="900" height="1200" viewBox="0 0 900 1200" aria-hidden="true">
    <polygon points="0,468 595,590 900,475 900,1200 0,1200" fill="#ffffff"/>
    <polygon points="0,438 595,560 900,453 900,475 595,590 0,468" fill="#11122e"/>
  </svg>

  <div class="brand">
    <div class="brand-dot"></div>
    <div class="brand-name">QBTREVOLT</div>
  </div>

  <h1 class="headline"><span class="line-1">FULL SERVICE</span><span class="line-2">APPLIANCE COMPANY</span></h1>
  <p class="showroom">Our showroom located at 14 N. Larkmoor Avenue<br>Fernwick, PA 18977.</p>

  <div class="web-pill">
    <div class="globe">
      <svg width="20" height="20" viewBox="0 0 20 20" aria-hidden="true"><circle cx="10" cy="10" r="9" fill="#ffffff"/><path d="M5 5c2 1 3 3 2 5s1 3 3 3M12 3c0 2 2 3 4 3M13 17c0-2 1-3 3-4" stroke="#11122e" stroke-width="1.6" fill="none"/></svg>
    </div>
    <span>WWW.QBTREVOLT.COM</span>
  </div>

  <div class="center-badge"></div>

  <h2 class="section-title" style="top:575px">ELECTRICAL CONTRACTING</h2>
  <p class="copy" style="left:62px; top:614px; width:355px;">Electrical systems are a very important element in everyone's home, and major appliances cannot function properly without a well installed and maintained electrical system. We offer electrical contracting services that ensure your home is safe and meets current code!</p>
  <p class="copy" style="left:62px; top:752px; width:355px;">Error sit voluptatem accusantium doloremque laudantium, totam rem aperiam, eaque ipsa quae ab illo inventore veritatis et quasi archite</p>

  <h2 class="section-title" style="top:853px">APPLIANCES</h2>
  <p class="copy" style="left:62px; top:895px; width:355px;">Error sit voluptatem accusantium doloremque laudantium, totam rem aperiam, eaque ipsa quae ab illo inventore veritatis et quasi archite</p>
  <p class="copy" style="left:62px; top:981px; width:224px;">Error sit voluptatem accusantium doloremque laudantium, totam rem aperiam, eaque ipsa</p>

  <div class="footer-band">
    <svg class="pin" width="22" height="30" viewBox="0 0 22 30" aria-hidden="true"><path d="M11 0C5 0 0 5 0 11c0 8 11 19 11 19s11-11 11-19C22 5 17 0 11 0z" fill="#ffffff"/><circle cx="11" cy="11" r="4" fill="#11122e"/></svg>
    <address>Qbtrevolt Home Electric<br>14 N. Larkmoor Avenue<br>Fernwick, PA 18977</address>
  </div>
  <div class="fridge-photo" role="img" aria-label="Photo of a stainless steel and a black bottom-freezer refrigerator"></div>

  <h2 class="provide-pill">WHAT WE PROVIDE</h2>
  <p class="copy" style="left:483px; top:738px; width:356px;">Error sit voluptatem accusantium doloremque laudantium, totam rem aperiam, eaque ipsa quae ab illo inventore veritatis et quasi architecto</p>
  <p class="copy" style="left:483px; top:832px; width:356px;">Atae vitae dicta sunt explicabo. Nemo enim ipsam voluptatem quia voluptas sit aspernatur aut odit aut fugit ed quia consequuntur magni dolores eos qui</p>

  <div class="services">
    <div class="service">
      <div class="service-icon"><svg width="30" height="22" viewBox="0 0 30 22" aria-hidden="true"><rect x="4" y="2" width="16" height="13" fill="#fff"/><path d="M20 6h5l4 5v4h-9z" fill="#fff"/><circle cx="9" cy="17" r="3" fill="#fff" stroke="#11122e" stroke-width="1.5"/><circle cx="24" cy="17" r="3" fill="#fff" stroke="#11122e" stroke-width="1.5"/><path d="M0 6h6M1 10h6" stroke="#fff" stroke-width="2"/></svg></div>
      <div class="service-label">WE DELIVER</div>
    </div>
    <div class="service">
      <div class="service-icon"><svg width="26" height="26" viewBox="0 0 26 26" aria-hidden="true"><path d="M4 4l18 18M22 4L4 22" stroke="#fff" stroke-width="3.5" stroke-linecap="round"/><circle cx="4" cy="4" r="3" fill="#fff"/></svg></div>
      <div class="service-label">INSTALL</div>
    </div>
    <div class="service">
      <div class="service-icon"><svg width="28" height="28" viewBox="0 0 28 28" aria-hidden="true"><path d="M14 3a10 10 0 0 0-9 14l-2 6 6-2a10 10 0 1 0 5-18z" fill="#fff"/><circle cx="9" cy="13" r="1.6" fill="#11122e"/><circle cx="14" cy="13" r="1.6" fill="#11122e"/><circle cx="19" cy="13" r="1.6" fill="#11122e"/></svg></div>
      <div class="service-label">SERVICE</div>
    </div>
    <div class="service">
      <div class="service-icon"><svg width="28" height="28" viewBox="0 0 28 28" aria-hidden="true"><circle cx="14" cy="14" r="12" fill="#fff"/><circle cx="14" cy="14" r="8" fill="none" stroke="#11122e" stroke-width="2"/><path d="M10 14l3 3 5-6" fill="none" stroke="#11122e" stroke-width="2.2" stroke-linecap="round"/></svg></div>
      <div class="service-label">WARRANTY</div>
    </div>
  </div>

  <div class="divider"></div>

  <div class="call">
    <svg width="50" height="50" viewBox="0 0 50 50" aria-hidden="true"><path d="M8 6l7-2 6 11-5 4c2 6 7 11 13 13l4-5 11 6-2 7c-2 4-8 5-14 2C17 36 10 28 6 18 4 12 5 8 8 6z" fill="none" stroke="#11122e" stroke-width="1.8" stroke-linejoin="round"/><path d="M30 16a6 6 0 0 1 5 5M31 10a11 11 0 0 1 10 10M32 4a16 16 0 0 1 15 15" fill="none" stroke="#11122e" stroke-width="1.8" stroke-linecap="round"/></svg>
    <div>
      <div class="call-label">CALL US:</div>
      <div class="call-number">(215) 846-3190</div>
    </div>
  </div>

  <div class="bottom-strip"></div>
</main>
</body>
</html>
```